Fiber To The Home

We want a 6x9 add front and back I like the ads I saw for Talvine. I want something that will stand out (Funny) but looks professional.

Target Market(s)

Residential

Requirements
Must have
• I'm not sure what I want. Our prices are on our website. I really like a few adds that I saw on here Talvine

```html
<!DOCTYPE html>
<html lang="en">
<head>
<meta charset="utf-8">
<title>Bresco Postcard – Front and Back</title>
<link href="https://fonts.googleapis.com/css2?family=Lato:wght@400;700&family=Oswald:wght@600&display=swap" rel="stylesheet">
<style>
  :root{
    --stage:#5d5b5c;
    --navy:#10224a;
    --navy-ink:#14264f;
    --blue:#4a72b8;
    --white:#ffffff;
    --ink:#1c1c1c;
    --grey-name:#8a8a8a;
    --stamp:#a9a9ab;
  }
  *{margin:0;padding:0;box-sizing:border-box}
  html,body{width:1200px;height:1200px;overflow:hidden;background:var(--stage);font-family:"Lato",sans-serif}
  .canvas{position:relative;width:1200px;height:1200px}
  .side-label{position:absolute;color:var(--white);font:700 36px "Lato",sans-serif}
  .side-label--front{left:830px;top:384px}
  .side-label--back{left:244px;top:898px}
  .card{position:absolute;background:var(--white);overflow:hidden;box-shadow:4px 6px 10px rgba(0,0,0,.35)}

  /* front */
  .card--front{left:60px;top:106px;width:683px;height:456px}
  .front-photo{position:absolute;left:0;top:0;width:440px;height:278px;
    background:linear-gradient(90deg,#c9ced8 0%,#b9c0cc 45%,#e7e9ee 80%,rgba(255,255,255,0) 100%)}
  .brand-name{font-family:"Lato",sans-serif;font-weight:700;color:var(--grey-name);letter-spacing:2px}
  .front-brand{position:absolute;left:406px;top:12px;font-size:44px}
  .headline{position:absolute;left:373px;top:80px;font:600 38px/42px "Oswald",sans-serif;color:var(--navy-ink);text-transform:uppercase}
  .intro{position:absolute;left:373px;top:170px;width:292px;font-size:11.2px;line-height:14px;color:var(--ink);text-align:justify}
  .contact-pill{position:absolute;left:369px;top:234px;width:305px;height:23px;border-radius:12px;background:var(--navy);
    color:var(--white);font-size:17px;display:flex;align-items:center;gap:7px;padding-left:12px}
  .band{position:absolute;left:0;top:264px}
  .feature{position:absolute;color:var(--white)}
  .feature h3{font-size:15px;font-weight:700;margin-bottom:12px;white-space:nowrap}
  .feature p{font-size:11.2px;line-height:14px}
  .feature--business{left:39px;top:350px;width:198px}
  .feature--home{left:294px;top:349px;width:158px}
  .feature--internet{left:503px;top:350px;width:156px}
  .feature--internet p{font-weight:700}

  /* back */
  .card--back{left:427px;top:656px;width:695px;height:462px}
  .back-brand{position:absolute;left:30px;top:30px;font-size:58px}
  .return-address{position:absolute;left:396px;top:22px;font-size:8px;color:var(--ink);display:flex;align-items:center;gap:5px}
  .stamp-box{position:absolute;left:621px;top:8px;width:58px;height:64px;background:var(--stamp)}
  .address-line{position:absolute;left:491px;width:193px;height:2px;background:var(--ink)}
  .back-photo{position:absolute;left:0;top:155px;width:388px;height:307px;
    background:linear-gradient(90deg,#33466f 0%,#6b7899 40%,#c8ccd6 75%,#e9e9ec 100%)}
  .services-tab{position:absolute;left:0;top:136px}
  .services-title{position:absolute;left:10px;top:141px;color:var(--white);font-size:26px;font-weight:700}
  .services-list{position:absolute;left:10px;top:193px;list-style:none}
  .services-list li{display:flex;align-items:center;gap:6px;height:30px;color:var(--white);font-size:12.5px;text-transform:uppercase;white-space:nowrap}
  .contact-strip{position:absolute;left:0;top:380px;width:388px;height:82px;
    background:linear-gradient(90deg,#4a72b8 0%,#4a72b8 45%,rgba(74,114,184,0) 70%)}
  .contact-list{position:absolute;left:16px;top:386px;list-style:none;color:var(--white);font-size:12px}
  .contact-list li{display:flex;align-items:center;gap:9px;height:22px;white-space:nowrap}
</style>
</head>
<body>
<main class="canvas">

  <span class="side-label side-label--front">Front</span>
  <span class="side-label side-label--back">Back</span>

  <section class="card card--front" aria-label="Postcard front">
    <div class="front-photo" role="img" aria-label="Businessman at a desk with a monitor holding a glass globe, over a faint world map background"></div>
    <div class="brand-name front-brand">BRESCO</div>
    <h1 class="headline">Your success is<br>our business</h1>
    <p class="intro">Serving local residents and businesses for more than 15 years. Providing internet &amp; satellite services to residential homes, commercial businesses, and multi-dwelling unit properties.</p>
    <div class="contact-pill">
      <span>Contact us @</span>
      <svg width="17" height="17" viewBox="0 0 20 20" aria-hidden="true"><circle cx="10" cy="10" r="9" fill="none" stroke="#fff" stroke-width="1.4"/><path d="M7 5.5l1.6 2.2-1 1.1c.6 1.3 1.5 2.2 2.7 2.8l1.1-1 2.1 1.6-.8 1.5c-3.2-.3-6.2-3.4-6.4-6.6z" fill="#fff"/></svg>
      <span>+1 555-013-2740</span>
    </div>

    <svg class="band" width="683" height="192" viewBox="0 264 683 192" aria-hidden="true">
      <rect x="0" y="278" width="683" height="168" fill="var(--blue)"/>
      <polygon points="240,264 448,264 490,360 464,446 238,446 275,360" fill="var(--navy)"/>
      <polyline points="240,264 275,360 238,446" fill="none" stroke="#fff" stroke-width="2"/>
      <polyline points="448,264 490,360 464,446" fill="none" stroke="#fff" stroke-width="2"/>
      <rect x="0" y="446" width="683" height="10" fill="var(--navy)"/>
      <g fill="none" stroke="#fff" stroke-width="1.3">
        <circle cx="113" cy="313" r="20"/>
        <circle cx="358" cy="310" r="20"/>
        <circle cx="586" cy="315" r="20"/>
      </g>
      <path d="M106 302l12-3v24l-12 3z" fill="var(--navy)"/>
      <path d="M346 311l12-11 12 11h-4v9h-16v-9z" fill="var(--blue)"/>
      <g fill="none" stroke="var(--navy)" stroke-width="1.6">
        <circle cx="586" cy="315" r="12"/>
        <ellipse cx="586" cy="315" rx="5" ry="12"/>
        <line x1="574" y1="315" x2="598" y2="315"/>
        <line x1="576" y1="309" x2="596" y2="309"/>
        <line x1="576" y1="321" x2="596" y2="321"/>
      </g>
    </svg>

    <div class="feature feature--business">
      <h3>BUSINESS SOLUTIONS</h3>
      <p>Internet To Designing and InSstalling a Secure Network, We've Got You Covered</p>
    </div>
    <div class="feature feature--home">
      <h3>HOME SOLUTIONS</h3>
      <p>Simple, All-Inclusive Pricing. Everything You Want, nothing You Don't.</p>
    </div>
    <div class="feature feature--internet">
      <h3>UNLIMITED INTERNET</h3>
      <p>No Data Caps Stream All You Want, TheSky's The Limit</p>
    </div>
  </section>

  <section class="card card--back" aria-label="Postcard back">
    <div class="brand-name back-brand">BRESCO</div>
    <div class="return-address">
      <svg width="11" height="13" viewBox="0 0 12 16" aria-hidden="true"><path d="M6 0a6 6 0 0 1 6 6c0 4-6 10-6 10S0 10 0 6a6 6 0 0 1 6-6z" fill="#555"/><circle cx="6" cy="6" r="2.3" fill="#fff"/></svg>
      <span>1400 Alder Rd Fenwick, Tennessee</span>
    </div>
    <div class="stamp-box"></div>
    <div class="address-line" style="top:214px"></div>
    <div class="address-line" style="top:246px"></div>
    <div class="address-line" style="top:276px"></div>

    <div class="back-photo" role="img" aria-label="Smiling businesswoman in glasses resting her chin on her hand in a bright office"></div>
    <svg class="services-tab" width="182" height="45" viewBox="0 0 182 45" aria-hidden="true">
      <polygon points="0,0 158,0 182,22 168,45 0,45" fill="var(--blue)"/>
    </svg>
    <div class="services-title">Our Services</div>
    <ul class="services-list">
      <li><svg width="9" height="11" viewBox="0 0 9 11" aria-hidden="true"><path d="M1 1l6 4.5L1 10" fill="none" stroke="#fff" stroke-width="2.2"/></svg>Experienced service technicians</li>
      <li><svg width="9" height="11" viewBox="0 0 9 11" aria-hidden="true"><path d="M1 1l6 4.5L1 10" fill="none" stroke="#fff" stroke-width="2.2"/></svg>Custom business solutions</li>
      <li><svg width="9" height="11" viewBox="0 0 9 11" aria-hidden="true"><path d="M1 1l6 4.5L1 10" fill="none" stroke="#fff" stroke-width="2.2"/></svg>Latest in technology</li>
      <li><svg width="9" height="11" viewBox="0 0 9 11" aria-hidden="true"><path d="M1 1l6 4.5L1 10" fill="none" stroke="#fff" stroke-width="2.2"/></svg>Exceptional customer service</li>
      <li><svg width="9" height="11" viewBox="0 0 9 11" aria-hidden="true"><path d="M1 1l6 4.5L1 10" fill="none" stroke="#fff" stroke-width="2.2"/></svg>No long term contract</li>
      <li><svg width="9" height="11" viewBox="0 0 9 11" aria-hidden="true"><path d="M1 1l6 4.5L1 10" fill="none" stroke="#fff" stroke-width="2.2"/></svg>Plans that fit every budget</li>
    </ul>
    <div class="contact-strip"></div>
    <ul class="contact-list">
      <li><svg width="15" height="15" viewBox="0 0 20 20" aria-hidden="true"><circle cx="10" cy="10" r="9" fill="none" stroke="#fff" stroke-width="1.4"/><path d="M7 5.5l1.6 2.2-1 1.1c.6 1.3 1.5 2.2 2.7 2.8l1.1-1 2.1 1.6-.8 1.5c-3.2-.3-6.2-3.4-6.4-6.6z" fill="#fff"/></svg>+1 555-013-2740</li>
      <li><svg width="15" height="13" viewBox="0 0 16 13" aria-hidden="true"><rect x="0.5" y="2" width="15" height="10.5" fill="#fff"/><path d="M0.5 2l7.5 6 7.5-6" fill="none" stroke="#4a72b8" stroke-width="1.2"/></svg>office@brescosatellite.tv</li>
      <li><svg width="15" height="15" viewBox="0 0 20 20" aria-hidden="true"><circle cx="10" cy="10" r="8.5" fill="none" stroke="#fff" stroke-width="1.6"/><line x1="1.5" y1="10" x2="18.5" y2="10" stroke="#fff" stroke-width="1.4"/><ellipse cx="10" cy="10" rx="4" ry="8.5" fill="none" stroke="#fff" stroke-width="1.4"/></svg>www.brescosatellite.tv</li>
    </ul>
  </section>

</main>
</body>
</html>
```